High-End Print/Digital Ad for Unique Luxury Travel Company Required

Objective:
Design a compelling and visually striking advertisement that highlights our company’s unmatched luxury travel experiences. The ad should elevate our brand image, spark curiosity, and drive prospective clients to contact us.
Target Audience:
• Affluent individuals seeking extraordinary, tailor-made travel experiences
• Affluent, luxury, high-net-worth individuals looking for value, expertise, and white-glove service
• Professionals or retirees who appreciate unique, thoughtfully curated travel over mainstream tourism
Key Messages to Communicate:
• One-of-a-kind luxury travel: Once-in-a-lifetime experiences that are curated with creativity and meticulous attention to detail
• Exceptional service: White-glove, personalized planning from start to finish
• 38 years’ travel experience – expert knowledge of destinations, modes of travel, premium accommodations and well-established, meaningful industry connections.
• Highly trusted: Cruise line executives often say, “No one does what you do.”
Tone and Style:
• Elegant, luxurious, sophisticated
• Eye-catching, polished, and modern
• Professional but warm—conveys trust and credibility
• High-impact visuals (full-bleed imagery, custom graphics, or high-end photography)
Deliverables:
• One full-page print ad and digital ad
• Ready-to-print, high-resolution file + working file (PSD, AI, etc.)
Optional: Social media-optimized version or short motion-graphic variation (if designer offers it)
Inspiration & Visual Style Suggestions:
• Think Velvet Voyager, Brimley Hart Wanderer, Seven Lanterns, or Oriel Retreats ad styles
• Large, emotive imagery with elegant typography
• Clean layout that speaks luxury, clarity, and trust
Copy Direction (draft):
For those who’ve explored the world—and crave something beyond the ordinary.
Each journey is a masterfully curated experience, rich in detail, seamless in execution, and unforgettable in every way.
Founded in 1997, Tidewell Journeys is a unique travel company specializing in cruising, all-inclusive luxury properties, and tours world-wide for individuals, groups, and incentives.
We offer an exceptional range of services designed to ensure every journey is flawlessly executed and truly unforgettable.
Let us help you plan your next extraordinary adventure.
Note: You may refine the copy slightly based on layout or format needs.
Other Resources for References:
1. Website - www.tidewelljourneys.example

```html
<!DOCTYPE html>
<html lang="en">
<head>
<meta charset="utf-8">
<title>Tidewell Journeys — Full-Page Ad</title>
<link href="https://fonts.googleapis.com/css2?family=Fraunces:opsz,wght@9..144,800&family=Oswald:wght@600&family=Poppins:wght@300;400;600;800&family=Open+Sans:wght@300&display=swap" rel="stylesheet">
<style>
  :root {
    --navy: #1b4a84;
    --navy-deep: #163d73;
    --orange: #f28d1e;
    --gold: #c2822a;
    --blue: #0d74bd;
    --yellow: #f7ec00;
    --body: #454545;
    --paper: #ffffff;
  }
  * { margin: 0; padding: 0; box-sizing: border-box; }
  html, body { width: 953px; height: 1200px; overflow: hidden; background: var(--paper); }
  .ad { position: relative; width: 953px; height: 1200px; overflow: hidden; background: var(--paper); }

  .hero-photo {
    position: absolute; left: 0; top: 196px; width: 953px; height: 712px;
    background:
      linear-gradient(180deg, #ffffff 0%, rgba(255,255,255,0) 10%),
      radial-gradient(ellipse 70% 18% at 50% 10%, #fbe7a6 0%, rgba(251,231,166,0) 100%),
      radial-gradient(ellipse 30% 40% at 22% 45%, #5c7a2c 0%, rgba(92,122,44,0) 100%),
      radial-gradient(ellipse 28% 35% at 82% 55%, #6b8a34 0%, rgba(107,138,52,0) 100%),
      radial-gradient(ellipse 25% 30% at 85% 25%, #e8914f 0%, rgba(232,145,79,0) 100%),
      radial-gradient(ellipse 30% 25% at 50% 70%, #c9b7c2 0%, rgba(201,183,194,0) 100%),
      linear-gradient(180deg, #f6e7c4 8%, #d9b48a 25%, #b98a5e 45%, #9c7a55 60%, #b79d96 75%, #e2b04e 100%);
  }

  .curves { position: absolute; left: 0; top: 0; width: 953px; height: 1200px; }

  .headline { position: absolute; left: 0; top: 38px; width: 925px; text-align: center; }
  .headline-lead {
    font-family: "Fraunces", Georgia, serif; font-weight: 800;
    font-size: 46px; line-height: 1; color: var(--navy); letter-spacing: -0.5px;
  }
  .headline-main {
    font-family: "Fraunces", Georgia, serif; font-weight: 800;
    font-size: 68px; line-height: 1; color: var(--orange); margin-top: 4px; letter-spacing: -0.5px;
  }
  .headline-sub {
    font-family: "Poppins", Arial, sans-serif; font-weight: 400;
    font-size: 24px; line-height: 1.2; color: var(--navy); margin-top: 6px;
  }

  .cta { position: absolute; left: 516px; top: 694px; width: 320px; text-align: center; }
  .cta-lead { font-family: "Poppins", Arial, sans-serif; font-weight: 300; font-size: 28px; line-height: 1.1; color: var(--navy); }
  .cta-plan { font-family: "Oswald", Impact, sans-serif; font-weight: 600; font-size: 44px; line-height: 1.05; color: var(--gold); letter-spacing: 0.5px; margin-top: 4px; }
  .cta-extra { font-family: "Poppins", Arial, sans-serif; font-weight: 800; font-size: 32px; line-height: 1.05; color: var(--navy); }

  .intro { position: absolute; left: 144px; top: 868px; width: 260px; font-family: "Poppins", Arial, sans-serif; }
  .intro-lead { font-weight: 600; font-size: 13px; line-height: 15.5px; color: var(--navy); position: absolute; left: -72px; top: 0; width: 260px; }
  .intro-body { font-family: "Open Sans", Arial, sans-serif; font-weight: 300; font-size: 11.6px; line-height: 15.2px; color: var(--body); position: absolute; left: -72px; top: 88px; width: 260px; }

  .divider { position: absolute; left: 431px; top: 866px; width: 1px; height: 156px; background: #bfc6cf; }

  .brand { position: absolute; left: 460px; top: 868px; width: 340px; text-align: center; }
  .brand-name {
    display: inline-flex; align-items: center; gap: 10px;
    font-family: "Poppins", Arial, sans-serif; font-weight: 600; font-size: 28px;
    line-height: 1; color: var(--navy); letter-spacing: 0.5px;
  }
  .brand-dot { width: 22px; height: 22px; border-radius: 50%; background: var(--navy); flex: none; }
  .brand-offer {
    font-family: "Poppins", Arial, sans-serif; font-weight: 300; font-size: 13.2px;
    line-height: 17px; color: var(--body); margin-top: 36px;
  }
  .brand-url {
    font-family: "Poppins", Arial, sans-serif; font-weight: 600; font-size: 13.5px;
    color: var(--navy); letter-spacing: 1.2px; margin-top: 18px;
  }
</style>
</head>
<body>
<main class="ad">
  <div class="hero-photo" role="img" aria-label="Sunset view over a colourful mosaic park with gingerbread-style pavilions, palm trees, visitors walking a plaza and a city skyline beyond"></div>

  <svg class="curves" viewBox="0 0 953 1200" aria-hidden="true">
    <defs>
      <linearGradient id="band-blue" x1="0" y1="0" x2="1" y2="0">
        <stop offset="0" stop-color="#0b6fb8"/>
        <stop offset="1" stop-color="#1f4f8f"/>
      </linearGradient>
      <linearGradient id="foot-blue" x1="0" y1="0" x2="1" y2="0">
        <stop offset="0" stop-color="#0a78c2"/>
        <stop offset="1" stop-color="#1c4683"/>
      </linearGradient>
    </defs>
    <path class="photo-band" d="M0,846 C230,796 470,786 953,838 L953,908 C700,832 360,814 0,886 Z" fill="url(#band-blue)"/>
    <path class="panel" d="M0,886 C360,814 700,832 953,908 L953,1200 L0,1200 Z" fill="#ffffff"/>
    <circle class="cta-bubble" cx="676" cy="803" r="167" fill="#ffffff"/>
    <path class="foot-wave" d="M0,1090 C190,1150 430,1180 953,1146 L953,1200 L0,1200 Z" fill="url(#foot-blue)"/>
    <path class="foot-gap" d="M240,1128 C480,1166 740,1160 953,1112 L953,1146 C430,1180 300,1160 240,1128 Z" fill="#ffffff"/>
    <path class="foot-accent" d="M282,1128 C500,1158 750,1150 953,1108 L953,1134 C740,1166 480,1160 282,1128 Z" fill="var(--yellow)"/>
  </svg>

  <header class="headline">
    <h1 class="headline-lead">For those who’ve</h1>
    <p class="headline-main">explored the world</p>
    <p class="headline-sub">and crave something beyond the ordinary</p>
  </header>

  <section class="cta">
    <p class="cta-lead">Let us help you</p>
    <p class="cta-plan">PLAN YOUR NEXT</p>
    <p class="cta-extra">Extraordinary<br>Adventure</p>
  </section>

  <section class="intro">
    <p class="intro-lead">Each journey is a<br>masterfully curated experience,<br>rich in detail, seamless in execution,<br>and unforgettable in every way.</p>
    <p class="intro-body">Founded in 1997, Tidewell Journeys is a unique travel company specializing in cruising, all-inclusive luxury properties, and tours world-wide for individuals, groups, and incentives.</p>
  </section>

  <div class="divider"></div>

  <section class="brand">
    <p class="brand-name"><span class="brand-dot"></span>Tidewell Journeys</p>
    <p class="brand-offer">We offer an exceptional range of services<br>designed to ensure every journey is flawlessly<br>executed and truly unforgettable.</p>
    <p class="brand-url">www.tidewelljourneys.example</p>
  </section>
</main>
</body>
</html>
```